Broschüre für Anbieter von Haushaltshilfen und Alltagsbegleitern für Privathaushalte
Zielgruppe
Wir bieten Haushaltshilfen und Alltagsbegleiter für Privathaushalte an. Unsere Hauptkundenklientel sind Pflegebedürftige Menschen denen eine Haushaltshilfe von der Pflegekasse zusteht. Weitere Kunden sind Familien und/oder Singlehaushalte, die eine Haushaltfshilfe benötigen.
Aufgabenstellung
- Das Prospekt sollte DIN A4 sein, sind aber auch offen für andere Formate
- Farbdesign muß unsere Logofarben enthalten
- In dem Prospekt müßen unsere Leistungen wie auf unserer Internetseite www.lindaufeld.de beschrieben sein.
- Seitenanzahl insgesamt 4 Seiten

```html
<!DOCTYPE html>
<html lang="de">
<head>
<meta charset="utf-8">
<title>Lindaufeld – Faltblatt Außenseite</title>
<link href="https://fonts.googleapis.com/css2?family=Montserrat:wght@300;400;700;800&display=swap" rel="stylesheet">
<style>
  :root {
    --brand-red: #be1622;
    --ink-dark: #3b2a2b;
    --paper: #ffffff;
    --stage: #f2f2f2;
    --fold-line: #e4e4e4;
  }
  * { margin: 0; padding: 0; box-sizing: border-box; }
  html, body { width: 1200px; height: 1200px; overflow: hidden; background: var(--stage); }
  body { position: relative; font-family: "Montserrat", sans-serif; }

  .spread {
    position: absolute; left: 40px; top: 204px;
    width: 1476px; height: 1043px;
    transform: scale(0.7588); transform-origin: 0 0;
    background: var(--paper);
    box-shadow: 0 6px 18px rgba(0,0,0,.18);
    overflow: hidden;
  }
  .panel { position: absolute; top: 0; height: 100%; }
  .panel--back { left: 0; width: 482px; border-right: 1px solid var(--fold-line); }
  .panel--inner { left: 482px; width: 495px; border-right: 1px solid var(--fold-line); }
  .panel--cover { left: 977px; width: 499px; }

  .photo-cleaning {
    position: absolute; left: 0; top: 0; width: 482px; height: 966px;
    border-bottom-right-radius: 26px;
    background: linear-gradient(160deg, #a88a5f 0%, #8e7a55 35%, #9a8f6b 60%, #5a2c22 100%);
  }

  .brand-mark {
    position: absolute; left: 0; right: 0; top: 270px;
    display: flex; align-items: center; justify-content: center; gap: 12px;
    color: var(--brand-red); font-weight: 700; font-size: 30px; letter-spacing: 1px;
  }
  .brand-mark__dot { width: 22px; height: 22px; border-radius: 50%; background: var(--brand-red); }

  .contact-card {
    position: absolute; left: 52px; top: 440px; width: 392px; height: 610px;
    background: var(--brand-red); border-radius: 22px 22px 0 0;
    padding: 68px 0 0 25px; color: var(--paper);
  }
  .question { font-size: 27px; line-height: 28px; text-transform: uppercase; }
  .question .light { font-weight: 400; color: var(--ink-dark); }
  .question .bold { font-weight: 800; color: var(--paper); }
  .contact-card__cta { margin: 78px 0 0 24px; font-size: 19px; font-weight: 400; }
  .contact-list { list-style: none; margin: 26px 0 0 24px; }
  .contact-list li { display: flex; align-items: flex-start; gap: 14px; font-size: 21px; line-height: 26px; margin-bottom: 14px; }
  .contact-list svg { width: 26px; height: 26px; flex: none; fill: var(--paper); }

  .photo-care {
    position: absolute; left: 0; top: 0; width: 499px; height: 600px;
    background: linear-gradient(135deg, #6b4a3a 0%, #c9a990 40%, #d9cabc 70%, #b9a89c 100%);
  }
  .title-banner {
    position: absolute; left: 28px; top: 549px; width: 471px; height: 178px;
    background: var(--brand-red); border-radius: 24px 0 0 24px;
    padding: 56px 0 0 31px; text-transform: uppercase;
  }
  .title-banner .light { display: block; font-weight: 400; font-size: 33px; line-height: 34px; color: var(--ink-dark); }
  .title-banner .bold { display: block; font-weight: 800; font-size: 38px; line-height: 40px; color: var(--paper); }
  .cover-brand {
    position: absolute; left: 0; right: 0; top: 880px;
    display: flex; align-items: center; justify-content: center; gap: 12px;
    color: var(--brand-red); font-weight: 700; font-size: 28px; letter-spacing: 1px;
  }
  .cover-brand .brand-mark__dot { width: 20px; height: 20px; }

  .decor { position: absolute; left: 0; top: 0; pointer-events: none; }
</style>
</head>
<body>
  <main class="spread">
    <section class="panel panel--back">
      <div class="photo-cleaning" role="img" aria-label="Foto: Frau saugt einen Teppich im Wohnzimmer neben einem Ledersofa"></div>
    </section>

    <section class="panel panel--inner">
      <div class="brand-mark"><span class="brand-mark__dot"></span>LINDAUFELD</div>
      <div class="contact-card">
        <h2 class="question">
          <span class="light">Sie sind</span><br>
          <span class="bold">Pflegebedürftig</span><br>
          <span class="light">und benötigen</span><br>
          <span class="bold">Hilfe im Haushalt?</span>
        </h2>
        <p class="contact-card__cta">Jetzt kostenlos beraten lassen!</p>
        <ul class="contact-list">
          <li><svg viewBox="0 0 24 24"><path d="M6.6 10.8a15 15 0 0 0 6.6 6.6l2.2-2.2c.3-.3.7-.4 1-.2 1.1.4 2.3.6 3.6.6.6 0 1 .4 1 1V20c0 .6-.4 1-1 1A17 17 0 0 1 3 4c0-.6.4-1 1-1h3.5c.6 0 1 .4 1 1 0 1.3.2 2.5.6 3.6.1.3 0 .7-.2 1z"/></svg>0711 98 76 54 32</li>
          <li><svg viewBox="0 0 24 24"><path d="M2 5h20v14H2zm2 2v.4l8 5.3 8-5.3V7zm0 2.8V17h16V9.8l-8 5.3z"/></svg>info@lindaufeld.de</li>
          <li><svg viewBox="0 0 24 24"><path d="M12 2a10 10 0 0 0-8.6 15l-1.4 5 5.1-1.3A10 10 0 1 0 12 2zm0 18a8 8 0 0 1-4.2-1.2l-.3-.2-3 .8.8-2.9-.2-.3A8 8 0 1 1 12 20zm4.4-6c-.2-.1-1.4-.7-1.6-.8s-.4-.1-.5.1l-.7.9c-.1.2-.3.2-.5.1a6.5 6.5 0 0 1-3.2-2.8c-.2-.4.2-.4.7-1.3.1-.2 0-.3 0-.4l-.7-1.7c-.2-.4-.4-.4-.5-.4h-.5a.9.9 0 0 0-.7.3 2.8 2.8 0 0 0-.9 2.1 5 5 0 0 0 1 2.6 11 11 0 0 0 4.3 3.8c1.6.7 2.2.7 3 .6.5-.1 1.4-.6 1.6-1.1s.2-1 .1-1.1z"/></svg>0176 123 456 78</li>
          <li><svg viewBox="0 0 24 24"><path d="M12 2a7 7 0 0 0-7 7c0 5 7 13 7 13s7-8 7-13a7 7 0 0 0-7-7zm0 9.5A2.5 2.5 0 1 1 12 6.5a2.5 2.5 0 0 1 0 5z"/></svg><span>Kastanienweg 14<br>73999 Ahrendorf</span></li>
        </ul>
      </div>
    </section>

    <section class="panel panel--cover">
      <div class="photo-care" role="img" aria-label="Foto: junge Betreuerin und lächelnde Seniorin sitzen gemeinsam am Tisch"></div>
      <h1 class="title-banner">
        <span class="light">Haushaltshilfen &amp;</span>
        <span class="bold">Alltagsbegleiter</span>
      </h1>
      <div class="cover-brand"><span class="brand-mark__dot"></span>LINDAUFELD</div>
    </section>

    <svg class="decor" width="1476" height="1043" viewBox="0 0 1476 1043" aria-hidden="true">
      <path d="M213 1043 A 275 275 0 0 1 534 814" fill="none" stroke="#be1622" stroke-width="2"/>
      <path d="M1476 0 V 110 A 140 140 0 0 1 1434 0 Z" fill="#be1622"/>
      <path d="M1360 0 A 150 150 0 0 0 1476 132" fill="none" stroke="#ffffff" stroke-width="2.5"/>
      <path d="M1392 727 A 90 90 0 0 1 1476 700" fill="none" stroke="#3b2a2b" stroke-width="2"/>
    </svg>
  </main>
</body>
</html>
```